Eye Catching Stylish Seminar Flyer

Design a Business Seminar Flyer that will be used for Print and Web distribution that is professional, eye catching in its color scheme and fonts.

have www.brightledgerday.com to register

Target Market(s)

Who is this for: business owners, marketplace professionals, homemakers.

Industry/Entity Type

Business Consultant

Font styles to use
Serif

Colors
abd037

Requirements
Must have
• Great colors, great Font
Nice to have
• Design a simple professional text based Logo for the Event that encapsulates For the flyer. Eye catching designs that provoke action in the reader of the flyer.
Should not have
• Cross designs stereotypical designs that are associated with religion. Rather they should be creative toward people that own businesses and work with colleagues in a daily office, school etc.

```html
<!DOCTYPE html>
<html lang="en">
<head>
<meta charset="utf-8">
<title>Moving From Intimacy to Impact – Seminar Flyer</title>
<link href="https://fonts.googleapis.com/css2?family=Libre+Baskerville&family=Open+Sans:wght@400;700&family=Varela+Round&display=swap" rel="stylesheet">
<style>
  :root {
    --paper: #ffffff;
    --panel-grey: #f2f2f3;
    --charcoal: #3a3a3c;
    --rust: #c94a27;
    --rust-dark: #8e2f16;
    --crimson: #9b1b30;
    --ink: #111111;
    --light-text: #f4f4f4;
  }
  html, body {
    margin: 0;
    padding: 0;
    width: 1043px;
    height: 1200px;
    overflow: hidden;
    background: var(--paper);
  }
  .flyer {
    position: relative;
    width: 1043px;
    height: 1200px;
    background: var(--paper);
    overflow: hidden;
    font-family: "Open Sans", Arial, sans-serif;
  }
  .headline {
    position: absolute;
    top: 22px;
    left: 0;
    width: 100%;
    text-align: center;
    margin: 0;
  }
  .headline__theme {
    font-family: "Varela Round", Arial, sans-serif;
    font-weight: 400;
    font-size: 39px;
    color: var(--ink);
    margin: 0;
    letter-spacing: 0.5px;
  }
  .headline__lead {
    font-family: "Libre Baskerville", Georgia, serif;
    color: var(--crimson);
    font-size: 29px;
    margin: 18px 0 0;
    padding-left: 0;
    margin-right: 8px;
  }
  .headline__title {
    font-family: "Libre Baskerville", Georgia, serif;
    color: var(--crimson);
    font-size: 53px;
    margin: 6px 0 0;
    letter-spacing: 0.5px;
  }
  .headline__title .connector {
    font-size: 34px;
  }
  .hero-photo {
    position: absolute;
    top: 185px;
    left: 0;
    width: 1043px;
    height: 425px;
    background:
      linear-gradient(to bottom, #ffffff 0%, rgba(255,255,255,0) 18%),
      linear-gradient(to bottom, #e9ebec 0%, #bfc2c2 40%, #8d8f88 62%, #7b7a72 75%, #5f6061 100%);
  }
  .shapes {
    position: absolute;
    left: 0;
    top: 0;
  }
  .brand {
    position: absolute;
    left: 30px;
    top: 640px;
    width: 210px;
    text-align: center;
  }
  .brand__mark {
    display: block;
    width: 56px;
    height: 56px;
    margin: 0 auto 18px;
    background: var(--crimson);
  }
  .brand__name {
    font-family: "Libre Baskerville", Georgia, serif;
    color: var(--crimson);
    font-size: 29px;
    line-height: 1.15;
    margin: 0;
  }
  .schedule, .lineup, .pricing {
    position: absolute;
    right: 56px;
    text-align: right;
    color: var(--light-text);
    margin: 0;
  }
  .schedule {
    top: 603px;
    font-size: 25px;
    line-height: 36px;
  }
  .lineup {
    top: 708px;
    right: 64px;
    font-size: 25px;
    line-height: 38px;
    list-style: none;
    padding: 0;
  }
  .lineup__label { font-weight: 700; }
  .lineup strong { font-weight: 700; }
  .pricing {
    top: 993px;
    font-size: 25px;
    line-height: 39px;
  }
  .pricing__url {
    display: block;
    margin-top: 18px;
    color: var(--rust);
    font-size: 25px;
    text-decoration: none;
  }
</style>
</head>
<body>
<main class="flyer">
  <header class="headline">
    <p class="headline__theme">The Voice of The LORD in the Marketplace</p>
    <p class="headline__lead">MOVING FROM</p>
    <h1 class="headline__title">INTIMACY <span class="connector">TO</span> IMPACT</h1>
  </header>

  <div class="hero-photo" role="img" aria-label="Businessman in a suit crouched in a sprinter's start position on an open road with mountains behind"></div>

  <svg class="shapes" width="1043" height="1200" viewBox="0 0 1043 1200" aria-hidden="true">
    <polygon points="0,608 1043,608 1043,1200 0,1200" fill="var(--panel-grey)"/>
    <polygon points="436,586 1043,586 1043,688 374,688" fill="var(--charcoal)"/>
    <polygon points="203,960 1043,960 1043,1200 65,1200" fill="var(--charcoal)"/>
    <polygon points="175,960 203,960 200,972" fill="var(--rust-dark)"/>
    <polygon points="328,688 1043,688 1043,960 175,960" fill="var(--rust)"/>
  </svg>

  <div class="brand">
    <span class="brand__mark"></span>
    <p class="brand__name">BRIGHT<br>LEDGER</p>
  </div>

  <p class="schedule">MARCH 24TH 6PM-9:20PM<br>MARCH 25TH 8:30AM-2:20PM</p>

  <ul class="lineup">
    <li class="lineup__label">FEATURING</li>
    <li><strong>Marcus Ellery:</strong> Author/Podcaster</li>
    <li><strong>Daniel Reyes:</strong> Business leader/Trainer</li>
    <li><strong>Clara Ellery:</strong> Writer</li>
    <li><strong>Sofia Navarro:</strong> Business Owner</li>
    <li><strong>Thomas Grady:</strong> Business Owner</li>
  </ul>

  <p class="pricing">FEE: $30<br>Includes continental breakfast, lunch, and light<br>refreshments throughout the conference.
    <a class="pricing__url" href="https://www.brightledgerday.com">BRIGHTLEDGERDAY.COM</a>
  </p>
</main>
</body>
</html>
```